Flyer-Design für nachhaltige Familienberatung
Reiche Ideenvielfalt (viele sehr verschiedene Designvorschläge), prompte Umsetzung aller Änderungsideen während und nach dem Wettbewerb und dazu ein sehr freundlicher Kontakt - so macht die Zusammenarbeit wirklich Spaß! Vielen Dank dafür!
Zielgruppe
Ich bin Kleinunternehmerin und berate junge Familien (auch Schwangere, Alleinerziehende und andere Angehörige) zu den Themen Stoffwindeln, Windelfrei, Babyschlaf und bedürfnis-/bindungsorientierter Erziehung. Außerdem biete ich Paarberatung und Einzelcoaching für Mütter und - gemeinsam mit meinem Mann - für Väter an.
Der Name 'Familie MiTi' steht für Mirja und Till, mich und meinem Mann, gleichzeitig ein Wortspiel mit einer 'Hasenfamilie', auf das gern angespielt werden kann.
Weitere Informationen zum Angebot können der Internetseite www.familie-miti.example entnommen werden.
Aufgabenstellung
Das Design sollte farblich und stilistisch zum Logo passen. Naturverbundenheit/Nachhaltigkeit und Familienleben/Geborgenheit dürfen im Mittelpunkt stehen.
Mein Angebot ist vielfältig - umso wichtiger ist eine übersichtliche klare Darstellung. Der Flyer sollte junge Familien ansprechen. Er sollte hochwertig und liebevoll wirken: die Leser*innen sollten ermutigt werden, mich einfach unverbindlich anzurufen/mir zu schreiben (E-Mail, Signal, WhatsApp, Facebook-Messenger) und mehr über das Angebot zu erfahren.
Die Flyer werden vor allem in Geburtshäusern, Krankenhäusern, Familienzentren und bei Frauen-/Kinderärzt*innen und Hebammen ausliegen. Außerdem werden sie durch Kooperationspartner*innen (Still-/Trageberaterinnen, in Geburtsvorbereitungskursen) verteilt.
Die hochgeladenen Fotos dürfen, müssen aber nicht verwendet werden.

```html
<!DOCTYPE html>
<html lang="de">
<head>
<meta charset="utf-8">
<title>Familienberatung Flyer</title>
<link href="https://fonts.googleapis.com/css2?family=Montserrat:wght@300;400;500&family=Quicksand:wght@400;500&display=swap" rel="stylesheet">
<style>
  :root {
    --paper: #ffffff;
    --backdrop: #e6e6e6;
    --peach: #f0d2b7;
    --ink: #333333;
    --ink-soft: #555555;
    --grey-light: #8a8a8a;
    --accent: #e8833a;
    --brand: #e07b2c;
  }
  * { margin: 0; padding: 0; box-sizing: border-box; }
  html, body { width: 862px; height: 1200px; overflow: hidden; }
  body { background: var(--backdrop); position: relative; font-family: "Quicksand", sans-serif; color: var(--ink); }

  .spread { position: absolute; left: 0; top: 297px; width: 862px; height: 607px; background: var(--paper); box-shadow: 0 4px 18px rgba(0,0,0,.12); }
  .spread-shapes { position: absolute; inset: 0; width: 862px; height: 607px; }

  .brand { position: absolute; left: 230px; top: 74px; width: 160px; text-align: center; display: flex; align-items: center; justify-content: center; gap: 6px; }
  .brand-dot { width: 9px; height: 9px; border-radius: 50%; background: var(--brand); }
  .brand-name { font-family: "Quicksand", sans-serif; font-weight: 500; font-size: 12px; letter-spacing: .08em; color: var(--brand); text-transform: uppercase; }

  .cover-title { position: absolute; left: 180px; top: 106px; width: 252px; text-align: center; font-family: "Montserrat", sans-serif; font-weight: 500; font-size: 30px; line-height: 33px; color: var(--ink); letter-spacing: .01em; }
  .cover-subtitle { position: absolute; left: 180px; top: 175px; width: 252px; text-align: center; font-family: "Montserrat", sans-serif; font-weight: 300; font-size: 13px; color: var(--grey-light); letter-spacing: .03em; }

  .service-list { position: absolute; right: 497px; top: 394px; list-style: none; text-align: right; font-size: 12.5px; color: var(--ink-soft); }
  .service-list li { line-height: 17px; }
  .service-list .rule { display: block; width: 24px; height: 1px; background: var(--accent); margin: 5px 0 6px auto; }

  .cover-intro { position: absolute; right: 497px; top: 473px; width: 210px; text-align: right; font-size: 10.5px; line-height: 14.5px; color: var(--ink-soft); }
  .cover-contact { position: absolute; right: 497px; top: 568px; font-size: 9.5px; color: var(--ink-soft); white-space: nowrap; word-spacing: 0; }
  .cover-contact span + span { margin-left: 9px; }

  .offer-heading { position: absolute; left: 488px; top: 182px; font-family: "Montserrat", sans-serif; font-weight: 300; font-size: 14px; color: var(--ink-soft); letter-spacing: .02em; }
  .offer-text { position: absolute; left: 488px; top: 217px; width: 283px; font-size: 9.4px; line-height: 13.4px; text-align: justify; color: var(--ink); }
  .offer-address, .offer-contact { position: absolute; left: 488px; font-size: 9.6px; line-height: 13.4px; color: var(--ink); font-style: normal; }
  .offer-address { top: 356px; }
  .offer-contact { top: 416px; }
</style>
</head>
<body>
<main class="spread">
  <svg class="spread-shapes" viewBox="0 0 1629 1147" preserveAspectRatio="none">
    <defs>
      <linearGradient id="photo-feet" x1="0" y1="0" x2="1" y2="1"><stop offset="0" stop-color="#4d5566"/><stop offset=".55" stop-color="#b59a6a"/><stop offset="1" stop-color="#d9c27a"/></linearGradient>
      <linearGradient id="photo-teddy" x1="0" y1="0" x2="1" y2="1"><stop offset="0" stop-color="#9a6a3f"/><stop offset=".5" stop-color="#7d5a44"/><stop offset="1" stop-color="#2f3f6e"/></linearGradient>
      <linearGradient id="photo-couple" x1="0" y1="0" x2="1" y2="1"><stop offset="0" stop-color="#5f7d3c"/><stop offset=".5" stop-color="#4b3f35"/><stop offset="1" stop-color="#8a9a55"/></linearGradient>
      <linearGradient id="photo-crawl" x1="0" y1="0" x2="0" y2="1"><stop offset="0" stop-color="#6e9a45"/><stop offset=".55" stop-color="#3e4a60"/><stop offset="1" stop-color="#8c7a6a"/></linearGradient>
      <linearGradient id="photo-sleep" x1="0" y1="0" x2="1" y2="1"><stop offset="0" stop-color="#f2e6da"/><stop offset=".5" stop-color="#e8c3a8"/><stop offset="1" stop-color="#d8c4a8"/></linearGradient>
    </defs>
    <!-- cover page -->
    <polygon fill="var(--peach)" points="0,0 272,272 0,544"/>
    <polygon fill="url(#photo-feet)" points="40,0 545,0 292,252" role="img" aria-label="Foto: Kinderfüße unter einer karierten Decke"/>
    <polygon fill="url(#photo-teddy)" points="292,290 572,567 292,847 12,567" role="img" aria-label="Foto: schlafendes Kleinkind mit Teddybär"/>
    <polygon fill="url(#photo-couple)" points="0,587 275,862 0,1137" role="img" aria-label="Foto: Elternpaar im Grünen"/>
    <polygon fill="var(--peach)" points="800,352 587,567 800,782"/>
    <!-- offer page -->
    <polygon fill="var(--peach)" points="1097,0 1629,0 1375,274"/>
    <polygon fill="url(#photo-crawl)" points="1397,290 1629,60 1629,527" role="img" aria-label="Foto: krabbelndes Kleinkind auf einem Holzsteg"/>
    <polygon fill="url(#photo-sleep)" points="1400,905 1629,652 1629,1120" role="img" aria-label="Foto: schlafendes Neugeborenes"/>
    <polygon fill="var(--peach)" points="1140,1147 1380,905 1625,1147"/>
  </svg>

  <section class="cover">
    <div class="brand"><span class="brand-dot"></span><span class="brand-name">Familie MiTi</span></div>
    <h1 class="cover-title">FAMILIEN<br>BERATUNG</h1>
    <p class="cover-subtitle">SPEZIELL FÜR EUCH</p>
    <ul class="service-list">
      <li>Beratung</li>
      <li class="rule" aria-hidden="true"></li>
      <li>Begleitung</li>
      <li class="rule" aria-hidden="true"></li>
      <li>Workshops</li>
    </ul>
    <p class="cover-intro">Wir möchten euch unterstützen, einen natürlichen und für euch passenden Weg als Familie zu finden. Egal wie viele Kinder, erziehend oder Regenbogenfamilie.</p>
    <p class="cover-contact"><span>mirja@familie-miti.example</span><span>0151 - 23456789</span><span>www.familie-miti.example</span></p>
  </section>

  <section class="offer">
    <h2 class="offer-heading">UNSER ANGEBOT</h2>
    <p class="offer-text">Abo et omnis volori arunda volore eost, si rero estem quis estio verumquos verum evendam, tectinctotae voloreic tem quis eic to enisciend pa aribus di simagni molupti atempor estrumquam alisquam nessum sum, totatet uresequos et quae eate qui officia simi, si sit ent quibus reiur, cuptium fugiam re, ex es estius, temquatis sed molloreperem et offictur, quibusam quo quo es non endaes aut quiduciur? Ovitiis eum, earum ulluptiae aperspelique dolupta simodit ipsum a dunt debis vendaepero doluptatur, optat doluptas coritios rem sita cus, con et ant omnimi, soluptatus.</p>
    <address class="offer-address">Familie MiTi<br>Mirja Welkert<br>Lindenweg 12<br>37000 Musterstadt</address>
    <p class="offer-contact">0151 - 23456789<br>mirja@familie-miti.example<br>www.familie-miti.example</p>
  </section>
</main>
</body>
</html>
```